Creative design for PLW Businesscard!

We would like a creative business card for our company The Maple Workshop. We situated in Barcelona and setup software development teams for companies in Belgium, Holland.

Orange is related to Holland.
PLW means cool in Dutch

* An Overview / Background of the Business & Services
o Setup and manage developer teams in Barcelona for for companies
in Holland, Belgium.
* The Target Market / Audience you are trying to reach
o Companies in Holland searching for developers
* Design Specifics; any preferences or ideas for Style, Colour,
Imagery, etc
o Orange, professional, fancy
o The Maple Workshop (PLW) means cool , good, nice

Target Market(s)

Companies in Holland searching for developers

Industry/Entity Type

Business

Contact Information for Business Card

Company name: The Maple Workshop

Name: Joost ter Haarveld

Title: Managing director (not necessary)

Email: joost@themapleworkshop.es

web: www.themapleworkshop.es

Phone: (+34) 932 487 113

Mobile: (+34) 668 302 947

Font styles to use
Other font styles liked:
• Bookman Old Style or Rockwell

Requirements
Must have
• Setup and manage developer teams in Barcelona for for companies
• in Holland, Belgium.

```html
<!DOCTYPE html>
<html lang="en">
<head>
<meta charset="utf-8">
<title>The Maple Workshop – Business Card</title>
<link rel="stylesheet" href="https://fonts.googleapis.com/css2?family=Montserrat:wght@500;700&display=swap">
<style>
  :root {
    --orange: #ec7035;
    --orange-deep: #dd3a0d;
    --orange-soft: #d9713a;
    --ink: #3a3a3a;
    --paper: #ffffff;
    --backdrop: #e4e4e4;
  }
  * { box-sizing: border-box; margin: 0; padding: 0; }
  html, body { width: 1200px; height: 800px; overflow: hidden; }
  body {
    background: var(--backdrop);
    font-family: "Montserrat", Arial, sans-serif;
    position: relative;
  }
  .card {
    position: absolute;
    width: 540px;
    height: 310px;
    box-shadow: 0 6px 18px rgba(0,0,0,0.18);
    overflow: hidden;
  }
  /* Front side */
  .card-front {
    left: 40px;
    top: 320px;
    background: var(--paper);
  }
  .brand {
    position: absolute;
    top: 40px;
    left: 0;
    right: 0;
    display: flex;
    justify-content: center;
    align-items: center;
    gap: 10px;
  }
  .brand-name {
    font-weight: 700;
    font-size: 52px;
    letter-spacing: 2px;
    color: var(--ink);
    line-height: 1;
  }
  .brand-dot {
    width: 22px;
    height: 22px;
    border-radius: 50%;
    background: var(--orange-soft);
  }
  .divider {
    position: absolute;
    top: 118px;
    left: 150px;
    width: 240px;
    height: 2px;
    background: var(--orange);
  }
  .person {
    position: absolute;
    top: 132px;
    left: 0;
    right: 0;
    text-align: center;
  }
  .person-name {
    font-weight: 700;
    font-size: 23px;
    color: var(--ink);
  }
  .person-title {
    font-weight: 500;
    font-size: 17px;
    color: var(--orange);
    margin-top: 2px;
  }
  .contacts {
    position: absolute;
    top: 196px;
    left: 0;
    right: 0;
    display: flex;
    justify-content: center;
    gap: 12px;
    font-size: 11px;
    font-weight: 500;
    color: var(--ink);
  }
  .contact { display: flex; align-items: center; gap: 4px; }
  .contact svg { width: 10px; height: 10px; fill: var(--orange); }
  .website {
    position: absolute;
    top: 214px;
    left: 0;
    right: 0;
    text-align: center;
    font-size: 11px;
    font-weight: 500;
    color: var(--ink);
  }
  .mark-placeholder {
    position: absolute;
    top: 236px;
    left: 254px;
    width: 32px;
    height: 26px;
    border-radius: 4px;
    background: var(--orange-soft);
    z-index: 2;
  }
  .swoosh {
    position: absolute;
    left: 0;
    bottom: 0;
    width: 540px;
    height: 70px;
  }
  /* Back side */
  .card-back {
    left: 620px;
    top: 170px;
    background: var(--orange);
  }
  .back-artwork {
    position: absolute;
    left: 200px;
    top: 95px;
    width: 150px;
    height: 120px;
    border-radius: 8px;
    background: linear-gradient(90deg, var(--orange-deep) 70%, #1e6a2a 100%);
  }
</style>
</head>
<body>
  <section class="card card-front" aria-label="Business card front">
    <div class="brand">
      <span class="brand-name">PLW</span>
      <span class="brand-dot"></span>
    </div>
    <div class="divider"></div>
    <div class="person">
      <p class="person-name">Joost ter Haarveld</p>
      <p class="person-title">Managing director</p>
    </div>
    <div class="contacts">
      <span class="contact">
        <svg viewBox="0 0 10 10" aria-hidden="true"><rect x="0" y="2" width="10" height="7" rx="1"/><path d="M0.5 2.5 L5 6 L9.5 2.5" stroke="#fff" stroke-width="0.8" fill="none"/></svg>
        joost@themapleworkshop.es
      </span>
      <span class="contact">
        <svg viewBox="0 0 10 10" aria-hidden="true"><path d="M1 3 Q5 0 9 3 L8 4.5 L6.5 4 L6.5 3.2 Q5 2.8 3.5 3.2 L3.5 4 L2 4.5 Z"/><rect x="2" y="5" width="6" height="4" rx="1"/></svg>
        (+34) 932 487 113
      </span>
      <span class="contact">
        <svg viewBox="0 0 10 10" aria-hidden="true"><rect x="2.5" y="0.5" width="5" height="9" rx="1" fill="none" stroke="#ec7035" stroke-width="1.2"/></svg>
        (+34) 668 302 947
      </span>
    </div>
    <p class="website">www.themapleworkshop.es</p>
    <div class="mark-placeholder" role="img" aria-label="Company emblem area"></div>
    <svg class="swoosh" viewBox="0 0 540 70" preserveAspectRatio="none" aria-hidden="true">
      <path d="M0 0 Q270 45 540 45 L540 70 L0 70 Z" fill="#d9713a"/>
    </svg>
  </section>

  <section class="card card-back" aria-label="Business card back">
    <div class="back-artwork" role="img" aria-label="Central fruit illustration with a green leaf"></div>
  </section>
</body>
</html>
```